Meadowgale Equine Hemp horse feed supplement LABEL

Design a label for a horse feed supplement made from hemp. American grown hemp, American made product, American owned company. This is targeted towards the race horse market, so a race horse graphic would be ideal.

Our slogan "The foundation of every healthy horse"

**When adding our logo, please change the lime green in our logo to #c1df7f **
Give TWO label options with the logo as described above and also an option with the word Equine removed from our logo.**
Updates

Target Market(s)

Performance Horses (Racing, team roping, cutting, reining, jumping)

Industry/Entity Type

Horseback Riding

Colors
eaf2ce
cadf82

Requirements
Must have
• - Meadowgale Equine Logo AS DESCRIBED in project description
- Checkboxes at the bottom with different size package choice (1lb, 5lb, 10lb, 25lb, 50lb) - We will hand mark the size when packaging

The following benefits of CBD:
- Anti-Inflammatory
- Pain Relief
- Anti-Anxiety
- Acid Neutralizer

Dosing Instructions:
750mg - Gastric care, joint support, inflammation, arthritis, and stress (1/2 Scoop)
1500mg - Chronic pain, seizures, severe arthritis, and intense anxiety (Full scoop)

Ingredients: Cannabis Sativa (Hemp)
Nice to have
• Would like to be able to stick a QR code on the label that will change between batches of hemp.

```html
<!DOCTYPE html>
<html lang="en">
<head>
<meta charset="utf-8">
<title>Meadowgale Equine Hemp – Pellet Labels</title>
<link rel="stylesheet" href="https://fonts.googleapis.com/css2?family=Cinzel:wght@600;700;800&family=Montserrat:wght@400;500;600;700&display=swap">
<style>
  :root {
    --backdrop: #e4e4e4;
    --label-white: #ffffff;
    --brown: #4b3526;
    --brown-deep: #3b2a1e;
    --lime: #9cc45a;
    --lime-soft: #c1df7f;
    --cream: #eaf2ce;
    --ink: #2a1f17;
  }
  * { box-sizing: border-box; margin: 0; padding: 0; }
  html, body {
    width: 1200px; height: 835px; overflow: hidden;
    background: var(--backdrop);
    font-family: "Montserrat", sans-serif;
  }
  .label-set {
    position: relative; width: 1200px; height: 835px;
    display: flex; justify-content: center; align-items: center; gap: 70px;
  }
  .label {
    position: relative; width: 450px; height: 790px;
    background: var(--label-white);
    border-radius: 14px;
    overflow: hidden;
    box-shadow: 0 4px 14px rgba(0,0,0,0.12);
    text-align: center;
    color: var(--ink);
  }
  .label p, .label h1, .label li { white-space: nowrap; }
  .seal-strip {
    position: absolute; left: 20px; right: 20px; top: 70px; height: 18px;
    border-top: 2px solid #ececec; border-bottom: 2px solid #ececec;
  }
  .brand-band {
    position: absolute; left: 0; right: 0; top: 122px; height: 118px;
    background: var(--brown);
    border-radius: 0 0 46px 46px;
    color: var(--label-white);
  }
  .brand-name {
    position: absolute; left: 0; right: 0; top: 34px;
    font-family: "Montserrat", sans-serif; font-weight: 600;
    font-size: 32px; line-height: 1.2; letter-spacing: 1px; color: var(--label-white);
  }
  .slogan {
    position: absolute; left: 0; right: 0; top: 92px;
    font-family: "Cinzel", serif; font-weight: 700;
    font-size: 12.5px; line-height: 1.2; letter-spacing: 0.5px;
  }
  .spectrum {
    position: absolute; left: 0; right: 0; top: 244px;
    font-family: "Cinzel", serif; font-weight: 700;
    font-size: 26px; line-height: 26px; color: var(--lime); letter-spacing: 1px;
  }
  .product-name {
    position: absolute; left: 0; right: 0; top: 270px;
    font-family: "Cinzel", serif; font-weight: 800;
    font-size: 88px; line-height: 1; color: var(--brown-deep); letter-spacing: -1px;
  }
  .format {
    position: absolute; left: 0; right: 0; top: 343px;
    font-weight: 700; font-size: 28px; line-height: 32px; color: var(--lime);
  }
  .audience {
    position: absolute; left: 0; right: 0; top: 374px;
    font-weight: 600; font-size: 17px; line-height: 20px; letter-spacing: 1px; color: var(--ink);
  }
  .disciplines {
    position: absolute; left: 0; right: 0; top: 396px;
    font-weight: 600; font-size: 11px; line-height: 14px; color: var(--lime);
  }
  .race-art {
    position: absolute; left: 100px; top: 418px; width: 240px; height: 134px;
    border-radius: 40% 50% 40% 45%;
    background: radial-gradient(ellipse at center, #cfc3b6 0%, #efe9e2 60%, var(--label-white) 100%);
  }
  .dosing-band {
    position: absolute; left: 18px; right: 18px; top: 558px; height: 14px;
    background: var(--lime-soft);
    border-top: 2px solid var(--lime); border-bottom: 2px solid var(--lime);
  }
  .dosing-title {
    position: absolute; left: 0; right: 0; top: 575px;
    font-family: "Cinzel", serif; font-weight: 700; font-size: 12px; line-height: 15px; color: var(--ink);
  }
  .dosing-list {
    position: absolute; left: 30px; right: 30px; top: 594px;
    display: flex; justify-content: space-between;
    list-style: none; font-size: 6.5px; line-height: 9px; font-weight: 600; text-transform: uppercase;
  }
  .dosing-list li::before { content: "• "; }
  .size-heading {
    position: absolute; left: 0; right: 0; top: 609px;
    font-weight: 500; font-size: 14px; line-height: 18px; letter-spacing: 1.6px; text-transform: uppercase;
  }
  .size-options {
    position: absolute; left: 50px; right: 50px; top: 630px;
    display: flex; justify-content: space-between; list-style: none;
    font-weight: 600; font-size: 11px; line-height: 14px; color: var(--lime);
  }
  .size-options li { display: flex; align-items: center; gap: 4px; }
  .size-options li::after {
    content: ""; width: 13px; height: 13px; border: 1.5px solid var(--ink); background: var(--label-white);
  }
  .benefits-band {
    position: absolute; left: 0; right: 0; top: 650px; height: 110px;
    background: var(--brown);
    border-radius: 46px 46px 0 0;
    color: var(--label-white);
  }
  .benefits-title {
    position: absolute; left: 0; right: 0; top: 14px;
    font-weight: 600; font-size: 15px; line-height: 18px; letter-spacing: 0.8px;
  }
  .benefits-list {
    position: absolute; left: 52px; right: 50px; top: 40px;
    display: grid; grid-template-columns: 1fr 1fr; row-gap: 7px;
    list-style: none; text-align: left; font-size: 11px; line-height: 14px; font-weight: 500;
  }
  .benefits-list li::before { content: "•"; margin-right: 8px; }
  .net-weight {
    position: absolute; left: 50%; top: 86px; transform: translateX(-50%);
    background: var(--label-white); color: var(--ink);
    font-weight: 700; font-size: 12px; line-height: 16px; padding: 3px 10px; border-radius: 8px 8px 0 0;
  }
</style>
</head>
<body>
<main class="label-set">
  <article class="label">
    <div class="seal-strip"></div>
    <header class="brand-band">
      <p class="brand-name">Meadowgale</p>
      <p class="slogan">THE FOUNDATION OF EVERY HEALTHY HORSE</p>
    </header>
    <p class="spectrum">Full Spectrum</p>
    <h1 class="product-name">HEMP</h1>
    <p class="format">Pellets</p>
    <p class="audience">PERFORMANCE HORSES</p>
    <p class="disciplines">(Racing, team roping, cutting, reining, jumping)</p>
    <div class="race-art" role="img" aria-label="Line illustration of a galloping race horse with jockey"></div>
    <div class="dosing-band"></div>
    <p class="dosing-title">Dosing Instructions:</p>
    <ul class="dosing-list">
      <li>Gastric care</li><li>Joint support</li><li>Arthritis</li><li>Inflammation</li><li>Stress (1/2 scoop)</li>
    </ul>
    <p class="size-heading">Different size package choice</p>
    <ul class="size-options">
      <li>1LB</li><li>5LB</li><li>10LB</li><li>25LB</li><li>50LB</li>
    </ul>
    <section class="benefits-band">
      <p class="benefits-title">BENEFITS OF CBD:</p>
      <ul class="benefits-list">
        <li>ANTI-INFLAMMATORY</li><li>PAIN RELIEF</li>
        <li>ANTI-ANXIETY</li><li>ACID NEUTRALIZER</li>
      </ul>
      <p class="net-weight">NET WET:750mg</p>
    </section>
  </article>

  <article class="label">
    <div class="seal-strip"></div>
    <header class="brand-band">
      <p class="brand-name">Meadowgale</p>
      <p class="slogan">THE FOUNDATION OF EVERY HEALTHY HORSE</p>
    </header>
    <p class="spectrum">Full Spectrum</p>
    <h1 class="product-name">HEMP</h1>
    <p class="format">Pellets</p>
    <p class="audience">PERFORMANCE HORSES</p>
    <p class="disciplines">(Racing, team roping, cutting, reining, jumping)</p>
    <div class="race-art" role="img" aria-label="Line illustration of a galloping race horse with jockey"></div>
    <div class="dosing-band"></div>
    <p class="dosing-title">Dosing Instructions:</p>
    <ul class="dosing-list">
      <li>Gastric care</li><li>Joint support</li><li>Arthritis</li><li>Inflammation</li><li>Stress (1/2 scoop)</li>
    </ul>
    <p class="size-heading">Different size package choice</p>
    <ul class="size-options">
      <li>1LB</li><li>5LB</li><li>10LB</li><li>25LB</li><li>50LB</li>
    </ul>
    <section class="benefits-band">
      <p class="benefits-title">BENEFITS OF CBD:</p>
      <ul class="benefits-list">
        <li>ANTI-INFLAMMATORY</li><li>PAIN RELIEF</li>
        <li>ANTI-ANXIETY</li><li>ACID NEUTRALIZER</li>
      </ul>
      <p class="net-weight">NET WET:1500mg</p>
    </section>
  </article>
</main>
</body>
</html>
```